Flyer-Design für Jungwinzergruppe
Zielgruppe
Wir sind eine Jungwinzergruppe und produzieren unsere eigenen Weine und Sekte. Unsere Zielgruppe ist gemischt aus jungen und älteren Leuten.

```html
<!DOCTYPE html>
<html lang="de">
<head>
<meta charset="utf-8">
<title>Die Jungwinzer – Flyer</title>
<link href="https://fonts.googleapis.com/css2?family=Jura:wght@500;700&family=Quicksand:wght@400;600;700&display=swap" rel="stylesheet">
<style>
:root{
  --wine:#9c3a48;
  --wine-dark:#7a2634;
  --wine-deep:#5e1c28;
  --paper:#f4f3f3;
  --text:#6a6a6a;
  --white:#ffffff;
  --stage:#e9e9e9;
  --photo-a:#6f6a5e;
  --photo-b:#3b3a3c;
}
*{box-sizing:border-box;margin:0;padding:0}
html,body{width:1200px;height:2534px;overflow:hidden}
body{background:var(--stage);font-family:"Quicksand",sans-serif;color:var(--text);position:relative}
.spread{position:absolute;left:30px;width:1140px;height:806px;display:flex;box-shadow:0 10px 30px rgba(0,0,0,.12)}
.spread--outside{top:401px}
.spread--inside{top:1327px}
.panel{position:relative;width:380px;height:806px;overflow:hidden}
.panel--light{background:var(--paper)}
.panel--wine{background:var(--wine);color:var(--white)}
.heading{font-family:"Jura",sans-serif;font-weight:700;font-size:22px;color:var(--wine);display:flex;align-items:center;gap:10px;justify-content:center;padding:8px 0;border-top:1.5px solid var(--wine);border-bottom:1.5px solid var(--wine);margin:0 30px}
.panel--wine .heading{color:var(--white);border-color:rgba(255,255,255,.7)}
.heading .dot{width:12px;height:12px;border-radius:50%;border:2px solid currentColor}
.copy{font-size:10.5px;line-height:1.45;margin-bottom:8px}
.copy strong{color:var(--wine);font-weight:700}
.lead{font-family:"Jura",sans-serif;font-weight:700;color:var(--wine);font-size:13.5px;line-height:1.25;margin:12px 0 8px}
.photo{position:absolute;display:block}
.round-photo{border-radius:50%;border:3px solid var(--white);background:radial-gradient(circle at 45% 40%,#bdbdbd,#4a4a4a)}
.brand{position:absolute;display:flex;align-items:center;gap:8px;font-family:"Jura",sans-serif;font-weight:700;font-size:20px;color:var(--white);letter-spacing:1px}
.brand .sq{width:14px;height:14px;background:var(--white)}
/* outside left */
.story{position:absolute;top:24px;left:0;right:0}
.story .body{padding:0 34px}
/* outside middle */
.about{position:absolute;top:330px;left:32px;right:32px;text-align:center}
.contact{position:absolute;top:520px;left:32px;right:32px}
.contact .name{font-family:"Jura",sans-serif;font-size:21px;line-height:1.05;margin:22px 0 16px 6px;letter-spacing:1px}
.contact .name small{font-size:16px;display:block}
.contact ul{list-style:none;font-weight:700;font-size:11px}
.contact li{display:flex;align-items:center;gap:10px;margin-bottom:8px}
.contact svg{flex:none}
/* cover */
.cover-title{position:absolute;top:400px;left:34px;right:34px;text-align:center}
.cover-title .rule{height:1.5px;background:rgba(255,255,255,.8)}
.cover-title h1{font-family:"Jura",sans-serif;font-weight:700;font-size:42px;margin:12px 0 4px;letter-spacing:.5px}
.cover-title p{font-family:"Jura",sans-serif;font-size:19px;letter-spacing:3px;margin-bottom:12px}
.url-pill{position:absolute;left:70px;bottom:28px;background:var(--wine);color:var(--white);font-family:"Jura",sans-serif;font-weight:700;font-size:15px;padding:7px 18px;border-radius:0 18px 18px 0}
/* inside left */
.pillars{position:absolute;top:275px;left:20px;right:20px;display:flex;justify-content:space-between;text-align:center}
.pillar{width:100px;font-family:"Jura",sans-serif;font-weight:700;color:var(--wine);font-size:13px;line-height:1.15}
.pillar .num{width:34px;height:34px;margin:0 auto 8px;border-radius:50%;background:var(--wine);color:var(--white);display:flex;align-items:center;justify-content:center;font-size:16px;border:3px double var(--white);outline:1.5px solid var(--wine)}
.wines{position:absolute;top:370px;left:34px;right:34px}
.wine-name{font-family:"Jura",sans-serif;font-weight:700;color:var(--wine);font-size:17px;margin:10px 0 4px}
.label{color:var(--wine);font-weight:700;text-transform:uppercase;font-size:10px}
/* inside middle */
.team{position:absolute;top:30px;left:0;right:0}
.member{display:flex;flex-direction:column;align-items:center;margin-top:28px}
.member .round-photo{width:128px;height:128px}
.member span{font-family:"Jura",sans-serif;font-weight:700;font-size:14px;margin-top:12px;padding:0 22px 6px;border-bottom:1.5px solid rgba(255,255,255,.8)}
/* inside right */
.bios{position:absolute;top:30px;left:0;right:0}
.bio{margin-bottom:26px}
.bio .copy{padding:0 34px;text-align:center;font-size:10px;margin:8px 0 6px}
</style>
</head>
<body>

<section class="spread spread--outside">
  <article class="panel panel--light">
    <div class="story">
      <h2 class="heading"><span class="dot"></span>Die Jungwinzer</h2>
      <div class="body">
        <p class="lead">Die neue Lese! – Drei junge Winzer – drei Philosophien – eine Leidenschaft</p>
        <p class="copy">Angefangen hat es im Jahre 2013. Die drei Jungs von der Ahr lernten sich in ihrer Ausbildung zum Winzer kennen. Schon damals war für sie klar, dass der Weinbau mehr als nur ein Beruf sein würde, und sie hatten erste eigene Ideen für ihren eigenen Wein.</p>
        <p class="copy">Sie taten sich zusammen und nannten sich fortan <strong>DIE JUNGWINZER – NEUE LESE</strong>, so steht es auch auf den recht außergewöhnlichen Etiketten ihrer Weinflaschen. Überhaupt zeigen schon ihre Etiketten, dass sie mit frischen Ideen an die Sache herangehen.</p>
        <p class="copy">Im ersten Schritt haben sie einen kleinen Weinberg mit alten Spätburgunder-Weinstöcken oberhalb vom Kaiserstuhl gepachtet, sukzessive sind noch einige Reihen dazu gekommen und inzwischen bearbeiten sie gemeinsam rund 3.500 m² Rebfläche.</p>
        <p class="copy">Den drei Jungwinzern geht es in erster Linie darum, durch neue, modernere und jüngere Interpretationen sowohl im Anbau wie auch im Ausbau der Weine ihren eigenen Stil zu entwickeln. Mit ihrer derzeitigen Rebfläche produzieren sie so jährlich rund 2.500 Flaschen Wein und Sekt.</p>
      </div>
    </div>
    <svg class="photo" style="left:0;bottom:0" width="380" height="250" viewBox="0 0 380 250" role="img" aria-label="Foto: die drei Jungwinzer sitzen mit Weinflaschen auf einer Weinbergmauer">
      <defs><linearGradient id="g-wall" x1="0" y1="0" x2="1" y2="1"><stop offset="0" stop-color="var(--photo-a)"/><stop offset="1" stop-color="var(--photo-b)"/></linearGradient></defs>
      <path d="M0 40 Q160 0 380 20 V250 H0 Z" fill="url(#g-wall)"/>
      <path d="M0 40 Q160 0 380 20 V32 Q160 14 0 58 Z" fill="var(--wine)"/>
    </svg>
  </article>

  <article class="panel panel--wine">
    <div class="round-photo photo" style="left:60px;top:30px;width:260px;height:260px" role="img" aria-label="Schwarz-Weiß-Foto: die drei Winzer an einem Weinfass mit Kerze"></div>
    <div class="brand" style="left:28px;top:30px"><span class="sq"></span>NEUE LESE</div>
    <p class="copy about">2013 gründeten wir, 3 Freunde von der Ahr, die gemeinsam die Ausbildung absolvierten, unser Jungwinzerprojekt, um unsere eigenen Ideen und Vorstellungen in Form eines Weines zu verwirklichen. Durch neue und jüngere Interpretationen des Anbaus und Ausbaus bildete sich unser eigener Stil. Diesen versuchen wir nun weiterzuentwickeln. Dabei versuchen wir die Tradition mit frischen Ideen zu ergänzen.</p>
    <div class="contact">
      <h2 class="heading"><span class="dot"></span>Ihr Weg zu uns</h2>
      <p class="name">Die Jungwinzer<small>die neue Lese</small></p>
      <ul>
        <li><svg width="10" height="14" viewBox="0 0 10 14"><path d="M5 0a5 5 0 0 1 5 5c0 4-5 9-5 9S0 9 0 5a5 5 0 0 1 5-5z" fill="#fff"/><circle cx="5" cy="5" r="1.8" fill="var(--wine)"/></svg>Lindenweg 8 | 53111 Talheim</li>
        <li><svg width="12" height="9" viewBox="0 0 12 9"><rect width="12" height="9" rx="1" fill="#fff"/><path d="M0 1l6 4 6-4" stroke="var(--wine)" fill="none"/></svg>info@neuelese-wein.de</li>
        <li><svg width="12" height="12" viewBox="0 0 12 12"><circle cx="6" cy="6" r="5.5" fill="#fff"/><path d="M1 6h10M6 .5c-3 3-3 8 0 11M6 .5c3 3 3 8 0 11" stroke="var(--wine)" fill="none"/></svg>www.neuelese-wein.de</li>
      </ul>
    </div>
  </article>

  <article class="panel panel--wine">
    <svg class="photo" style="left:0;top:0" width="380" height="330" viewBox="0 0 380 330" role="img" aria-label="Foto: die drei Jungwinzer stehen im Weinberg über dem Dorf">
      <defs><linearGradient id="g-hill" x1="0" y1="0" x2="0" y2="1"><stop offset="0" stop-color="#8f9180"/><stop offset="1" stop-color="#3c3d42"/></linearGradient></defs>
      <path d="M0 0 H380 V230 Q200 250 0 320 Z" fill="url(#g-hill)"/>
      <path d="M0 320 Q200 250 380 230 V250 Q200 262 0 330 Z" fill="var(--wine-deep)"/>
    </svg>
    <div class="brand" style="right:30px;top:344px"><span class="sq"></span>NEUE LESE</div>
    <div class="cover-title">
      <div class="rule"></div>
      <h1>Die Jungwinzer</h1>
      <p>Die neue Lese!</p>
      <div class="rule"></div>
    </div>
    <svg class="photo" style="left:0;bottom:0" width="380" height="250" viewBox="0 0 380 250" role="img" aria-label="Foto: die drei Jungwinzer sitzen mit Weinflaschen auf einer Weinbergmauer">
      <path d="M0 40 Q220 0 380 60 V250 H0 Z" fill="url(#g-wall)"/>
      <path d="M0 28 Q220 -12 380 48 V60 Q220 0 0 40 Z" fill="var(--wine-deep)"/>
    </svg>
    <div class="url-pill">www.neuelese-wein.de</div>
  </article>
</section>

<section class="spread spread--inside">
  <article class="panel panel--light">
    <svg class="photo" style="left:0;top:0" width="380" height="240" viewBox="0 0 380 240" role="img" aria-label="Foto: Weinflaschen und Weinglas auf Korken">
      <defs><linearGradient id="g-bottles" x1="0" y1="0" x2="1" y2="1"><stop offset="0" stop-color="#a58a66"/><stop offset="1" stop-color="#3d2f2a"/></linearGradient></defs>
      <path d="M0 0 H380 V200 Q200 150 0 240 Z" fill="url(#g-bottles)"/>
    </svg>
    <div class="pillars">
      <div class="pillar"><div class="num">3</div>verschiedene Philosophien</div>
      <div class="pillar"><div class="num">3</div>Junge Winzer</div>
      <div class="pillar"><div class="num">1</div>gemeinsame Leidenschaft</div>
    </div>
    <div class="wines">
      <p class="copy">Neben dem für das Ahrtal obligatorischen Spätburgunder haben wir einen Blanc de Noir und einen Sekt in unserer noch jungen Produktpalette.</p>
      <h3 class="wine-name">Blanc de Noir trocken</h3>
      <p class="copy"><span class="label">Charakterisierung:</span><br>Eleganter Blanc de Noir aus 100 % Spätburgunder Trauben. Zeichnet sich durch seine hohe Fruchtigkeit und frische Aromen aus. Die Trauben wachsen auf Schiefer, das gibt dem Wein eine mineralische Note.</p>
      <h3 class="wine-name">Spätburgunder trocken</h3>
      <p class="copy"><span class="label">Charakterisierung:</span><br>Typischer Ahr-Burgunder, der ausschließlich in Steillagen auf Schieferverwitterungsgestein gewachsen ist. Die Eleganz und Komplexität wird durch niedrige Erträge, selektive Lese und die Lagerung in kleinen Eichenholzfässern erreicht.</p>
    </div>
  </article>

  <article class="panel panel--wine">
    <div class="team">
      <h2 class="heading"><span class="dot"></span>Die Jungwinzer</h2>
      <div class="member"><div class="round-photo" role="img" aria-label="Porträtfoto Jonas Weidler"></div><span>Jonas Weidler</span></div>
      <div class="member"><div class="round-photo" role="img" aria-label="Porträtfoto Torben Vogt"></div><span>Torben Vogt</span></div>
      <div class="member"><div class="round-photo" role="img" aria-label="Porträtfoto Lukas Hammes an der Rebe"></div><span>Lukas Hammes</span></div>
    </div>
  </article>

  <article class="panel panel--light">
    <div class="bios">
      <section class="bio">
        <h2 class="heading"><span class="dot"></span>Jonas Weidler</h2>
        <p class="copy">Jonas absolvierte seine Ausbildung zum Winzer von 2010–2012 beim Weingut Hofmann in Marienthal. Von 2013 bis 2016 machte er sein Fachabitur für Agrarwirtschaft.</p>
        <p class="copy">Seitdem ist er als Winzer im Weingut Steinbach angestellt und sammelt wichtige Erfahrungen. Seit November 2018 macht er nebenbei die Ausbildung zum Wintermeister.</p>
        <p class="copy">Zum Weinbau ist er durch seinen Opa gekommen, der jahrzehntelang als Genossenschaftswinzer gearbeitet hat.</p>
      </section>
      <section class="bio">
        <h2 class="heading"><span class="dot"></span>Torben Vogt</h2>
        <p class="copy">Torben absolvierte seine Ausbildung zum Winzer von 2012–2015 beim Weingut Lehnert in Dernau.</p>
        <p class="copy">Von 2015 bis 2016 machte er sein Fachabitur für Agrarwirtschaft. Seit Herbst 2016 studiert er Weinbau und Oenologie an der Hochschule.</p>
        <p class="copy">Weinbau wird in der Familie Vogt in der fünften Generation betrieben. So ist es naheliegend, dass er in Zukunft ins elterliche Weingut einsteigen wird.</p>
      </section>
      <section class="bio">
        <h2 class="heading"><span class="dot"></span>Lukas Hammes</h2>
        <p class="copy">Lukas absolvierte seine Ausbildung zum Winzer von 2012–2015 beim Weingut Rebhang in Heppingen und beim örtlichen Winzerverein.</p>
        <p class="copy">Von 2015 bis 2016 machte er sein Fachabitur für Agrarwirtschaft. Seit Herbst 2016 studiert er Weinbau und Oenologie an der Hochschule.</p>
        <p class="copy">Zum Weinbau ist er durch seinen Onkel gekommen, der Kellermeister in einem der größten Weingüter der Ahr ist.</p>
      </section>
    </div>
  </article>
</section>

</body>
</html>
```